Law firm business card

Information:

Me Miriam Dufresne

website: dufresne-law.ca
email: miriam@dufresne-law.ca
Phone: 514 555-0147
Fax: 514 555-0183

Address:
Dufresne and associates
2719 Belcourt
Montreal, QC
H2K 3M9

Areas of Expertise:
Franchise Agreements, Financing, Acquisition, Real Estate Development, Commercial Agreements and Corporate Law

Target Market(s)

executives, companie managers

Industry/Entity Type

Business

Colors
f78f20
000000

Requirements
Must have
• Must use the logo, the logo is available here:

https://www.filebinder-example.com/sh/qxt8rr2ka41wpe/BBKtm7Lwzve_pQRYdNG_HJcWb

```html
<!DOCTYPE html>
<html lang="en">
<head>
<meta charset="utf-8">
<title>Dufresne &amp; Associates – Business Card</title>
<link rel="stylesheet" href="https://fonts.googleapis.com/css2?family=Exo+2:wght@400;500;600&display=swap">
<style>
  :root {
    --orange: #f78f20;
    --ink: #000000;
    --text: #333333;
    --rule: #9a9a9a;
    --card: #ffffff;
    --card-shade: #f1f1f1;
    --backdrop: #e6e6e6;
  }
  * { box-sizing: border-box; margin: 0; padding: 0; }
  html, body { width: 1200px; height: 750px; overflow: hidden; }
  body {
    background: var(--backdrop);
    font-family: "Exo 2", Arial, sans-serif;
    position: relative;
  }
  .card {
    position: absolute;
    top: 215px;
    width: 560px;
    height: 320px;
    background: linear-gradient(135deg, var(--card) 0%, var(--card-shade) 100%);
    box-shadow: 0 4px 14px rgba(0,0,0,0.12);
    overflow: hidden;
  }
  .card--front { left: 20px; }
  .card--back { left: 620px; }

  .wordmark {
    display: flex;
    align-items: center;
    gap: 12px;
  }
  .wordmark__disc {
    width: 46px; height: 46px;
    border: 2px solid var(--orange);
    border-radius: 50%;
    flex: none;
  }
  .wordmark__rule {
    width: 1px; height: 52px;
    background: var(--rule);
    flex: none;
  }
  .wordmark__name {
    color: var(--orange);
    font-weight: 500;
    text-transform: uppercase;
    line-height: 1.05;
  }
  .wordmark__name span { display: block; }
  .wordmark__line1 { font-size: 27px; letter-spacing: 0.5px; }
  .wordmark__line2 { font-size: 15px; letter-spacing: 2px; }

  .card--front .wordmark {
    position: absolute;
    left: 50%; top: 50%;
    transform: translate(-50%, -50%);
  }

  .card--back .wordmark {
    position: absolute;
    left: 40px; top: 118px;
  }
  .card--back .wordmark__disc { width: 40px; height: 40px; }
  .card--back .wordmark__rule { height: 46px; }
  .card--back .wordmark__line1 { font-size: 23px; }
  .card--back .wordmark__line2 { font-size: 13px; }

  .accent { position: absolute; inset: 0; }

  .person {
    position: absolute;
    right: 34px; top: 34px;
    text-align: right;
  }
  .person__name {
    color: var(--orange);
    font-size: 16px;
    font-weight: 500;
    letter-spacing: 1.5px;
    text-transform: uppercase;
  }
  .person__title {
    color: var(--ink);
    font-size: 11px;
    margin-top: 2px;
  }

  .contact {
    position: absolute;
    left: 92px; top: 190px;
    list-style: none;
  }
  .contact__item {
    display: flex;
    align-items: center;
    gap: 8px;
    font-size: 11px;
    color: var(--text);
    height: 18px;
  }
  .contact__icon { width: 11px; height: 11px; flex: none; }

  .address {
    position: absolute;
    right: 28px; bottom: 36px;
    text-align: right;
    color: #ffffff;
    font-size: 13px;
    font-style: normal;
    line-height: 1.35;
    letter-spacing: 0.3px;
  }
</style>
</head>
<body>

  <section class="card card--front" aria-label="Card front">
    <div class="wordmark">
      <div class="wordmark__disc"></div>
      <div class="wordmark__rule"></div>
      <div class="wordmark__name">
        <span class="wordmark__line1">Dufresne</span>
        <span class="wordmark__line2">&amp; Associates</span>
      </div>
    </div>
  </section>

  <section class="card card--back" aria-label="Card back">
    <svg class="accent" width="560" height="320" viewBox="0 0 560 320" aria-hidden="true">
      <polygon points="300,320 560,150 560,320" fill="var(--orange)"/>
      <line x1="272" y1="320" x2="560" y2="132" stroke="var(--orange)" stroke-width="2"/>
    </svg>

    <div class="person">
      <div class="person__name">Miriam Dufresne</div>
      <div class="person__title">Managing Director</div>
    </div>

    <div class="wordmark">
      <div class="wordmark__disc"></div>
      <div class="wordmark__rule"></div>
      <div class="wordmark__name">
        <span class="wordmark__line1">Dufresne</span>
        <span class="wordmark__line2">&amp; Associates</span>
      </div>
    </div>

    <ul class="contact">
      <li class="contact__item">
        <svg class="contact__icon" viewBox="0 0 12 12" aria-label="Phone"><path d="M2 1 L4.5 1 L5.5 3.5 L4 4.6 C4.6 6 6 7.4 7.4 8 L8.5 6.5 L11 7.5 L11 10 C11 10.6 10.6 11 10 11 C5 11 1 7 1 2 C1 1.4 1.4 1 2 1 Z" fill="var(--orange)"/></svg>
        514 555-0147
      </li>
      <li class="contact__item">
        <svg class="contact__icon" viewBox="0 0 12 12" aria-label="Mobile"><rect x="3" y="0.5" width="6" height="11" rx="1" fill="none" stroke="var(--orange)" stroke-width="1.2"/><circle cx="6" cy="9.6" r="0.7" fill="var(--orange)"/></svg>
        514 555-0162
      </li>
      <li class="contact__item">
        <svg class="contact__icon" viewBox="0 0 12 12" aria-label="Fax"><rect x="3" y="0.5" width="6" height="4" fill="var(--orange)"/><rect x="1" y="4.5" width="10" height="5" rx="1" fill="var(--orange)"/><rect x="3" y="8" width="6" height="3.5" fill="var(--orange)"/></svg>
        514 555-0183
      </li>
      <li class="contact__item">
        <svg class="contact__icon" viewBox="0 0 12 12" aria-label="Email"><rect x="0.5" y="2" width="11" height="8" fill="var(--orange)"/><path d="M0.8 2.4 L6 6.6 L11.2 2.4" fill="none" stroke="#ffffff" stroke-width="1"/></svg>
        miriam@dufresne-law.ca
      </li>
      <li class="contact__item">
        <svg class="contact__icon" viewBox="0 0 12 12" aria-label="Website"><circle cx="6" cy="6" r="5.5" fill="var(--orange)"/><circle cx="6" cy="6" r="2.5" fill="none" stroke="#ffffff" stroke-width="1"/></svg>
        dufresne-law.ca
      </li>
    </ul>

    <address class="address">
      2719 Belcourt<br>
      Montreal, QC H2K 3M9
    </address>
  </section>

</body>
</html>
```